Food Choices & Patient-Reported Outcomes in Parkinson's disease

We have spent the past 7 years studying food choices and rate of PD progression. We want to show people which foods have the most significant impact. <br/><br/>The infographic attached called "Community Wellness in QM" is the first in this 6-part series, recently designed by someone on PixelForge. I'd like this entire series to "pair nicely" with one another, but also have unique personality, which is why I've opened the contest up. <br/><br/>The VEX-QM scale is the point of reference, it explains that higher scores are worse, low scores are better. I'd like to stick with the green is good, red is bad theme. ish. <br/><br/>The blue bar chart with food is "the grand finale." THIS is the information people have been waiting for for decades! I expect this to be highly circulated-- passed to physicians, support groups, getting tens of thousands of shares online! Below, I uploaded the 2019 version (also produced by someone from Pixel Forge). On my ppt screen shot, that data on the bottom left is also REALLY important. Can make another bar chart? Or find some other creative way to communicate it? OK to not include the p-values (OK to remove the far right column). Thanks!

Target Market(s)

Patients, their partners/ families, and health care providers.

Requirements
Must have
• Must include the legend-- some version of the VEX-QM scale vs. Quality of Life, as a point of reference. If possible, I'd like to stick with [some shade of] green is good, with it being clear that scores are getting worse [red-ish] as the scores increase.
• Must have the website, so people can go look for more information/ details about the project.
Nice to have
• Coordination with the "Community Wellness ..." infographic below.

```html
<!DOCTYPE html>
<html lang="en">
<head>
<meta charset="utf-8">
<title>Food Choices &amp; Parkinson's Disease Progression</title>
<link href="https://fonts.googleapis.com/css2?family=Merriweather:ital,wght@0,700;0,900;1,400&family=Source+Sans+3:ital,wght@0,400;0,600;0,700;1,600&display=swap" rel="stylesheet">
<style>
  :root {
    --page: #e9e7ec;
    --card: #f7f7f7;
    --panel: #e4e4e6;
    --purple: #5f2a86;
    --pink: #f2c4d8;
    --ink: #1a1a1a;
    --black: #0d0d0d;
    --poor: #b71c2c;
    --fair: #ee7a5c;
    --good: #c6db7e;
    --excellent: #8cc152;
    --axis-band: #dedede;
    --green-dark: #1e6a34;
    --green-mid: #3f9a3e;
    --green-light: #8dc63f;
    --red: #e01f2d;
    --red-dark: #a8243a;
    --grid: #c9c9cc;
  }
  html, body {
    margin: 0;
    width: 1200px;
    height: 887px;
    overflow: hidden;
    background: var(--page);
  }
  .infographic {
    position: absolute;
    left: 0;
    top: 57px;
    width: 1200px;
    height: 772px;
    display: block;
  }
  .serif { font-family: "Merriweather", Georgia, serif; }
  .sans { font-family: "Source Sans 3", Arial, sans-serif; }
  .title-main { font-weight: 900; font-size: 29px; fill: #fff; }
  .title-year { font-weight: 900; font-size: 23px; fill: var(--purple); }
  .title-meta { font-style: italic; font-weight: 600; font-size: 15px; fill: #fff; }
  .title-url { font-weight: 700; font-size: 15.5px; fill: #fff; }
  .chart-title { font-weight: 700; font-size: 17px; fill: var(--ink); }
  .chart-sub { font-size: 10.5px; fill: var(--ink); }
  .axis-num { font-size: 15px; fill: var(--ink); }
  .axis-label { font-style: italic; font-weight: 700; font-size: 17px; fill: #fff; }
  .band-label { font-weight: 600; font-size: 21px; fill: #fff; }
  .x-caption { font-style: italic; font-weight: 600; font-size: 17px; fill: var(--ink); }
  .row-label { font-size: 11.5px; fill: var(--ink); }
  .pill-num { font-size: 9.5px; fill: #fff; }
  .side-caption { font-style: italic; font-weight: 700; font-size: 15px; fill: var(--ink); }
  .food-label { font-size: 11px; fill: var(--ink); }
  .legend-small { font-size: 8.5px; font-weight: 700; fill: var(--ink); }
  .legend-pill { font-size: 8.5px; fill: #fff; }
</style>
</head>
<body>
<svg class="infographic" viewBox="185 206 1109 713" xmlns="http://www.w3.org/2000/svg" preserveAspectRatio="none">
  <rect x="185" y="206" width="1109" height="713" fill="var(--card)"/>

  <!-- Title block -->
  <g class="title-block">
    <rect x="202" y="219" width="360" height="282" fill="var(--purple)"/>
    <rect x="202" y="219" width="360" height="9" fill="var(--pink)"/>
    <path d="M483 219 H562 V250 H500 Z" fill="var(--pink)"/>
    <text class="serif title-year" x="496" y="243">2020</text>
    <text class="serif title-main" x="224" y="290">Food Choices &amp;</text>
    <text class="serif title-main" x="224" y="323">Parkinson’s Disease</text>
    <text class="serif title-main" x="224" y="357">Progression</text>
    <text class="sans title-meta" x="224" y="388">RT Halvorsen et al.</text>
    <text class="sans title-meta" x="224" y="420" style="font-size:20px;font-style:normal;font-weight:700">...</text>
    <text class="sans title-meta" x="224" y="458">For study details:</text>
    <text class="serif title-url" x="224" y="479">www.NourishPDStudy.org</text>
  </g>

  <!-- Quality of life chart -->
  <g class="qol-chart">
    <text class="serif chart-title" x="957" y="239" text-anchor="middle">Correlation Between Quality of Life and VEX-QM Score</text>
    <rect x="579" y="253" width="33" height="205" fill="var(--black)"/>
    <text class="sans axis-label" transform="translate(602 360) rotate(-90)" text-anchor="middle">VEX-QM SCORE</text>
    <rect x="1240" y="253" width="34" height="205" fill="var(--black)"/>
    <text class="sans axis-label" transform="translate(1264 358) rotate(-90)" text-anchor="middle">Quality Of Life</text>
    <rect x="612" y="253" width="44" height="205" fill="var(--card)"/>
    <g class="sans axis-num" text-anchor="middle">
      <text x="634" y="277">2500</text>
      <text x="634" y="318">2000</text>
      <text x="634" y="358">1500</text>
      <text x="634" y="399">1000</text>
      <text x="638" y="439">500</text>
    </g>
    <rect x="656" y="253" width="580" height="94" fill="var(--poor)"/>
    <rect x="656" y="347" width="580" height="37" fill="var(--fair)"/>
    <rect x="656" y="384" width="580" height="36" fill="var(--good)"/>
    <rect x="656" y="420" width="580" height="38" fill="var(--excellent)"/>
    <g class="sans band-label" text-anchor="end">
      <text x="1214" y="309">Poor</text>
      <text x="1214" y="375">Fair</text>
      <text x="1214" y="411">Good</text>
      <text x="1214" y="448">Excellent</text>
    </g>
    <line x1="665" y1="420" x2="1128" y2="335" stroke="#fff" stroke-width="2.5"/>
    <g fill="#fff">
      <circle cx="713" cy="411" r="5"/><circle cx="784" cy="398" r="5"/>
      <circle cx="865" cy="383" r="5"/><circle cx="941" cy="368" r="5"/>
      <circle cx="1019" cy="354" r="5"/><circle cx="1102" cy="340" r="5"/>
    </g>
    <rect x="579" y="460" width="695" height="27" fill="var(--axis-band)"/>
    <g class="sans axis-num" text-anchor="middle">
      <text x="645" y="479">0</text><text x="713" y="479">5</text>
      <text x="788" y="479">10</text><text x="866" y="479">15</text>
      <text x="944" y="479">20</text><text x="1023" y="479">25</text>
      <text x="1101" y="479">30</text><text x="1180" y="479">35</text>
    </g>
    <line x1="584" y1="501" x2="865" y2="501" stroke="var(--ink)" stroke-width="1.3"/>
    <line x1="1037" y1="501" x2="1268" y2="501" stroke="var(--ink)" stroke-width="1.3"/>
    <path d="M580 501 l9 -4 v8 z M1274 501 l-9 -4 v8 z" fill="var(--ink)"/>
    <text class="sans x-caption" x="951" y="507" text-anchor="middle">Years Since Diagnosis</text>
  </g>

  <!-- Dietary behaviours -->
  <g class="behaviour-chart">
    <rect x="202" y="517" width="529" height="387" fill="var(--panel)"/>
    <text class="serif chart-title" x="462" y="547" text-anchor="middle" style="font-size:15.5px">Impact of dietary behaviours on PD progression</text>
    <text class="sans chart-sub" x="446" y="561" text-anchor="middle">N = 1503 - 1521 (per question, if answered)</text>
    <g stroke="var(--grid)" stroke-width="1">
      <line x1="236" y1="597" x2="665" y2="597"/><line x1="236" y1="623" x2="665" y2="623"/>
      <line x1="236" y1="649" x2="665" y2="649"/><line x1="236" y1="675" x2="665" y2="675"/>
      <line x1="236" y1="701" x2="665" y2="701"/><line x1="236" y1="727" x2="665" y2="727"/>
      <line x1="236" y1="753" x2="665" y2="753"/><line x1="236" y1="779" x2="665" y2="779"/>
      <line x1="236" y1="805" x2="665" y2="805"/><line x1="236" y1="831" x2="665" y2="831"/>
      <line x1="236" y1="857" x2="665" y2="857"/><line x1="236" y1="883" x2="665" y2="883"/>
    </g>
    <g class="sans row-label">
      <text x="237" y="588">I cook most of my meals</text>
      <text x="237" y="614">I avoid artificial sweetners</text>
      <text x="237" y="640">I avoid soda</text>
      <text x="237" y="666">I avoid artificial colors, flavors</text>
      <text x="237" y="692">I routinely prepare meals for others</text>
      <text x="237" y="718">I avoid dairy</text>
      <text x="237" y="744">I try to eat organically grown foods when possible</text>
      <text x="237" y="770">I avoid pork</text>
      <text x="237" y="796">I buy from local farmers</text>
      <text x="239" y="822">I avoid beef</text>
      <text x="237" y="848">I find it difficult to afford healthy food</text>
      <text x="237" y="874">It is difficult to afford groceries</text>
    </g>
    <rect x="236" y="592" width="150" height="5" fill="var(--green-dark)"/>
    <rect x="236" y="618" width="124" height="5" fill="var(--green-dark)"/>
    <rect x="236" y="644" width="107" height="5" fill="#2c7d37"/>
    <rect x="236" y="670" width="104" height="5" fill="#2c7d37"/>
    <rect x="236" y="696" width="101" height="5" fill="var(--green-mid)"/>
    <rect x="236" y="722" width="89" height="5" fill="var(--green-mid)"/>
    <rect x="236" y="748" width="75" height="5" fill="#5aab3d"/>
    <rect x="236" y="774" width="54" height="5" fill="#6db73e"/>
    <rect x="236" y="800" width="48" height="5" fill="#7cbf3f"/>
    <rect x="236" y="826" width="34" height="5" fill="var(--green-light)"/>
    <rect x="236" y="852" width="292" height="5" fill="var(--red)"/>
    <rect x="236" y="878" width="326" height="5" fill="var(--red-dark)"/>
    <rect x="665" y="573" width="24" height="324" rx="12" fill="var(--black)"/>
    <g class="sans pill-num" text-anchor="middle">
      <text x="677" y="594">-146</text><text x="677" y="619">-121</text>
      <text x="677" y="644">-108</text><text x="677" y="670">-106</text>
      <text x="677" y="696">-105</text><text x="677" y="722">-92</text>
      <text x="677" y="748">-86</text><text x="677" y="775">-75</text>
      <text x="677" y="800">-71</text><text x="677" y="826">-63</text>
      <text x="677" y="856">366</text><text x="677" y="886">389</text>
    </g>
    <text class="sans side-caption" transform="translate(712 731) rotate(-90)" text-anchor="middle">Estimated Impact On VEX-QM</text>
  </g>

  <!-- Food servings -->
  <g class="food-chart">
    <rect x="747" y="517" width="527" height="387" fill="var(--panel)"/>
    <text class="serif chart-title" x="1012" y="547" text-anchor="middle" style="font-size:15.5px">Impact of 2-4 servings per week on</text>
    <text class="serif chart-title" x="1012" y="564" text-anchor="middle" style="font-size:15.5px">Parkinson’s Disease Severity</text>
    <g class="bars">
      <rect x="801" y="630" width="8" height="221" fill="var(--green-dark)"/>
      <rect x="820" y="703" width="8" height="148" fill="#236f35"/>
      <rect x="839" y="716" width="8" height="135" fill="#2a7636"/>
      <rect x="858" y="723" width="8" height="128" fill="#327e37"/>
      <rect x="877" y="738" width="8" height="113" fill="#3f8a3a"/>
      <rect x="895" y="740" width="8" height="111" fill="#4a953b"/>
      <rect x="914" y="779" width="8" height="72" fill="#6cb13d"/>
      <rect x="933" y="801" width="8" height="50" fill="var(--green-light)"/>
      <rect x="952" y="822" width="8" height="29" fill="var(--red)"/>
      <rect x="970" y="812" width="8" height="39" fill="var(--red)"/>
      <rect x="989" y="807" width="8" height="44" fill="#dc1f2e"/>
      <rect x="1008" y="798" width="8" height="53" fill="#d8202f"/>
      <rect x="1026" y="794" width="8" height="57" fill="#d42030"/>
      <rect x="1045" y="790" width="8" height="61" fill="#d02131"/>
      <rect x="1064" y="787" width="8" height="64" fill="#cc2132"/>
      <rect x="1083" y="773" width="8" height="78" fill="#c82233"/>
      <rect x="1102" y="767" width="8" height="84" fill="#c42234"/>
      <rect x="1120" y="745" width="8" height="106" fill="#bf2335"/>
      <rect x="1139" y="736" width="8" height="115" fill="#ba2336"/>
      <rect x="1158" y="730" width="8" height="121" fill="#b52437"/>
      <rect x="1176" y="721" width="8" height="130" fill="#b02438"/>
      <rect x="1195" y="716" width="8" height="135" fill="#ac2439"/>
      <rect x="1214" y="687" width="8" height="164" fill="var(--red-dark)"/>
    </g>
    <g class="sans food-label">
      <text transform="translate(809 627) rotate(-90)">Fresh Vegetables</text>
      <text transform="translate(828 700) rotate(-90)">Fresh Fruit</text>
      <text transform="translate(847 713) rotate(-90)">Nuts/Seed</text>
      <text transform="translate(866 720) rotate(-90)">Fish</text>
      <text transform="translate(885 735) rotate(-90)">Wine</text>
      <text transform="translate(903 737) rotate(-90)">Olive Oil</text>
      <text transform="translate(922 776) rotate(-90)">Coconut oil</text>
      <text transform="translate(941 798) rotate(-90)">Fresh Herbs</text>
      <text transform="translate(960 819) rotate(-90)">Milk</text>
      <text transform="translate(978 809) rotate(-90)">Cheese</text>
      <text transform="translate(997 804) rotate(-90)">Yogurt</text>
      <text transform="translate(1016 795) rotate(-90)">Frozen Vegetables</text>
      <text transform="translate(1034 791) rotate(-90)">Pork</text>
      <text transform="translate(1053 787) rotate(-90)">Chicken</text>
      <text transform="translate(1072 784) rotate(-90)">Plastic-bottled drinks</text>
      <text transform="translate(1091 770) rotate(-90)">Soda</text>
      <text transform="translate(1110 764) rotate(-90)">Pasta</text>
      <text transform="translate(1128 742) rotate(-90)">Beef</text>
      <text transform="translate(1147 733) rotate(-90)">Canned Veg</text>
      <text transform="translate(1166 727) rotate(-90)">Ice Cream</text>
      <text transform="translate(1184 718) rotate(-90)">Fried Foods</text>
      <text transform="translate(1203 713) rotate(-90)">Diet Soda</text>
      <text transform="translate(1222 684) rotate(-90)">Canned Fruit</text>
    </g>
    <rect x="786" y="851" width="448" height="19" rx="9.5" fill="var(--black)"/>
    <g class="sans pill-num" text-anchor="middle">
      <text transform="translate(805 864) rotate(-45)">-225</text>
      <text transform="translate(824 864) rotate(-45)">-188</text>
      <text transform="translate(843 864) rotate(-45)">-161</text>
      <text transform="translate(862 864) rotate(-45)">-144</text>
      <text transform="translate(881 864) rotate(-45)">-115</text>
      <text transform="translate(899 864) rotate(-45)">-114</text>
      <text transform="translate(918 864) rotate(-45)">-79</text>
      <text transform="translate(937 864) rotate(-45)">-58</text>
      <text transform="translate(956 864) rotate(-45)">42</text>
      <text transform="translate(974 864) rotate(-45)">51</text>
      <text transform="translate(993 864) rotate(-45)">56</text>
      <text transform="translate(1012 864) rotate(-45)">63</text>
      <text transform="translate(1030 864) rotate(-45)">67</text>
      <text transform="translate(1049 864) rotate(-45)">68</text>
      <text transform="translate(1068 864) rotate(-45)">69</text>
      <text transform="translate(1087 864) rotate(-45)">84</text>
      <text transform="translate(1106 864) rotate(-45)">85</text>
      <text transform="translate(1124 864) rotate(-45)">106</text>
      <text transform="translate(1143 864) rotate(-45)">110</text>
      <text transform="translate(1162 864) rotate(-45)">120</text>
      <text transform="translate(1180 864) rotate(-45)">144</text>
      <text transform="translate(1199 864) rotate(-45)">146</text>
      <text transform="translate(1218 864) rotate(-45)">191</text>
    </g>
    <g class="legend">
      <line x1="792" y1="879" x2="942" y2="879" stroke="var(--green-light)" stroke-width="1.2"/>
      <path d="M789 879 l6 -3 v6 z M945 879 l-6 -3 v6 z" fill="var(--green-light)"/>
      <rect x="845" y="874" width="62" height="10" rx="5" fill="var(--green-light)"/>
      <text class="sans legend-pill" x="876" y="882" text-anchor="middle">-300 - 0</text>
      <text class="sans legend-small" x="875" y="893" text-anchor="middle">VEX - QM</text>
      <line x1="952" y1="879" x2="1230" y2="879" stroke="var(--red)" stroke-width="1.2"/>
      <path d="M949 879 l6 -3 v6 z M1233 879 l-6 -3 v6 z" fill="var(--red)"/>
      <rect x="1059" y="874" width="60" height="10" rx="5" fill="var(--red)"/>
      <text class="sans legend-pill" x="1089" y="882" text-anchor="middle">0 - 300</text>
      <text class="sans legend-small" x="1089" y="893" text-anchor="middle">VEX - QM</text>
    </g>
  </g>
</svg>
</body>
</html>
```